4K Business Card Design

We need a business card that emphasizes consulting services worldwide. The name of the company is KKKK Consulting Group. We provide consulting services across several industries including but not limited to commodities, telecom, manufacturing, logistics, marketing and operations. We would like to see a creative design that emphasizes the global aspect, including Latin America and US markets, as well the bilingual nature of the service offerings.

The contact information section should include icons to represent the following data:
1) Name, Title and Company Name
2) Mobile Number
3) Skype ID
4) Email
5) Web Page
6) Location

We would like to see a card that emphasizes the worldwide concept. The back of the card should be simple, including only the logo (or a portion of the logo) and the slogan.

We would also like to see business cards in a booklet format. The colors to be used should be the same combination of colors used in the logos attached to this brief.

The logo design and some business card examples from Artful Herd are attached for reference on style and look.

Target Market(s)

International business executives, 45-65 years of age, bilingual

Industry/Entity Type

Marketing

Colors
0792cd
34a7d8
85cae6
ffffff
cee9f5
ecf7fb

Requirements
Must have
• Please follow colors in logo attached.

2) Mobile Number
3) Skype ID
4) Email
5) Web Page
6) Location
Nice to have
• Global concept, consulting profile, diverse industry focus
Should not have
• No black color

```html
<!DOCTYPE html>
<html lang="en">
<head>
<meta charset="utf-8">
<title>KKKK Consulting Group – Business Card</title>
<link href="https://fonts.googleapis.com/css2?family=Arimo:wght@400;700&display=swap" rel="stylesheet">
<style>
  :root {
    --card-white: #ffffff;
    --card-tint: #ecf7fb;
    --name-strip: #cee9f5;
    --band-blue: #0792cd;
    --block-deep: #0792cd;
    --block-mid: #34a7d8;
    --block-light: #85cae6;
    --globe-line: #85cae6;
    --divider: #ffffff;
    --ink-navy: #0b4f72;
    --ink-light: #ffffff;
  }
  * { margin: 0; padding: 0; box-sizing: border-box; }
  html, body {
    width: 1200px;
    height: 659px;
    overflow: hidden;
    background: var(--card-white);
  }
  .business-card {
    position: relative;
    width: 1200px;
    height: 659px;
    background: linear-gradient(180deg, var(--card-white) 0%, var(--card-tint) 100%);
    font-family: "Arimo", Arial, sans-serif;
    overflow: hidden;
  }
  .corner-tab {
    position: absolute;
    left: 1068px;
    top: 22px;
    width: 132px;
    height: 70px;
    background: var(--name-strip);
  }
  .world-globe {
    position: absolute;
    left: 840px;
    top: 110px;
    width: 240px;
    height: 240px;
  }
  .name-strip {
    position: absolute;
    left: 55px;
    top: 212px;
    width: 640px;
    height: 76px;
    background: var(--name-strip);
  }
  .person-name {
    position: absolute;
    left: 130px;
    top: 220px;
    font-size: 54px;
    font-weight: 700;
    color: var(--ink-navy);
    letter-spacing: 0.5px;
    line-height: 60px;
  }
  .company-band {
    position: absolute;
    left: 0;
    top: 372px;
    width: 1200px;
    height: 98px;
    background: var(--band-blue);
    border-bottom: 6px solid var(--divider);
  }
  .company-name {
    position: absolute;
    left: 40px;
    top: 22px;
    font-size: 46px;
    font-weight: 700;
    color: var(--ink-light);
    letter-spacing: 1px;
  }
  .info-block {
    position: absolute;
    top: 476px;
    height: 183px;
    font-size: 20px;
    line-height: 26px;
    display: flex;
    flex-direction: column;
    justify-content: center;
    gap: 12px;
  }
  .info-row {
    display: flex;
    align-items: center;
    gap: 12px;
    white-space: nowrap;
  }
  .info-icon {
    width: 24px;
    height: 24px;
    flex: none;
  }
  .info-block--title {
    left: 0;
    width: 400px;
    background: var(--block-deep);
    color: var(--ink-light);
    padding-left: 40px;
  }
  .info-block--online {
    left: 406px;
    width: 370px;
    background: var(--block-mid);
    color: var(--ink-light);
    padding-left: 30px;
  }
  .info-block--phone {
    left: 782px;
    width: 418px;
    background: var(--block-light);
    color: var(--ink-navy);
    padding-left: 40px;
  }
</style>
</head>
<body>
  <main class="business-card">
    <div class="corner-tab"></div>

    <svg class="world-globe" viewBox="0 0 240 240" role="img" aria-label="Outline globe for worldwide reach">
      <g fill="none" stroke="var(--globe-line)" stroke-width="3">
        <circle cx="120" cy="120" r="110"/>
        <ellipse cx="120" cy="120" rx="50" ry="110"/>
        <line x1="120" y1="10" x2="120" y2="230"/>
        <line x1="10" y1="120" x2="230" y2="120"/>
        <path d="M25 65 H215 M25 175 H215"/>
      </g>
    </svg>

    <div class="name-strip"></div>
    <h1 class="person-name">Lena Quintero</h1>

    <section class="company-band">
      <h2 class="company-name">KKKK Consulting Group</h2>
    </section>

    <section class="info-block info-block--title">
      <div class="info-row">
        <svg class="info-icon" viewBox="0 0 24 24" aria-hidden="true"><circle cx="12" cy="8" r="4.5" fill="currentColor"/><path d="M3 22c0-5 4-8 9-8s9 3 9 8z" fill="currentColor"/></svg>
        <div><p>President &amp; CEO,</p><p>KKKK Counsulting Group</p></div>
      </div>
    </section>

    <section class="info-block info-block--online">
      <div class="info-row">
        <svg class="info-icon" viewBox="0 0 24 24" aria-hidden="true"><rect x="2" y="5" width="20" height="14" rx="2" fill="none" stroke="currentColor" stroke-width="2"/><path d="M3 6l9 7 9-7" fill="none" stroke="currentColor" stroke-width="2"/></svg>
        <span>k4cg@brightmail.com</span>
      </div>
      <div class="info-row">
        <svg class="info-icon" viewBox="0 0 24 24" aria-hidden="true"><path d="M4 4h16v11H10l-5 4v-4H4z" fill="none" stroke="currentColor" stroke-width="2" stroke-linejoin="round"/></svg>
        <span>k4consultinggroup</span>
      </div>
      <div class="info-row">
        <svg class="info-icon" viewBox="0 0 24 24" aria-hidden="true"><g fill="none" stroke="currentColor" stroke-width="2"><circle cx="12" cy="12" r="10"/><ellipse cx="12" cy="12" rx="4" ry="10"/><line x1="2" y1="12" x2="22" y2="12"/></g></svg>
        <span>www.k4consultinggroup.com</span>
      </div>
    </section>

    <section class="info-block info-block--phone">
      <div class="info-row">
        <svg class="info-icon" viewBox="0 0 24 24" aria-hidden="true"><rect x="6" y="2" width="12" height="20" rx="2" fill="none" stroke="currentColor" stroke-width="2"/><circle cx="12" cy="18" r="1.3" fill="currentColor"/></svg>
        <span>Mobile: +1 555 210-4837</span>
      </div>
      <div class="info-row">
        <svg class="info-icon" viewBox="0 0 24 24" aria-hidden="true"><path d="M12 22s7-7 7-12a7 7 0 0 0-14 0c0 5 7 12 7 12z" fill="currentColor"/><circle cx="12" cy="10" r="2.5" fill="var(--block-light)"/></svg>
        <span>Verano Shores, FL</span>
      </div>
    </section>
  </main>
</body>
</html>
```